Präsentationsvorlagen für eine internistisch-allgemeinmedizinische Arztpraxis
Zielgruppe
Wir sind eine internistisch-allgemeinmedizinische Arztpraxis
Die Folien werden sowohl für Fachvortröge aber auch für Patientenvorträge genutzt
Aufgabenstellung
Hätte gerne einen Vorschlag für 2 Versionen Format 16:9 und 4:3
Des Weiteren hätte ich gerne einen Bereich in der Präsentation wo man Studien/Literaturzutate ersichtlich darstellen kann.

```html
<!DOCTYPE html>
<html lang="de">
<head>
<meta charset="utf-8">
<title>Praxis am Lindengrund – Präsentationsvorlage</title>
<link rel="stylesheet" href="https://fonts.googleapis.com/css2?family=Montserrat:wght@400;500;600;700&display=swap">
<style>
:root{
  --stage:#5b6564;
  --white:#ffffff;
  --blue:#1f5b96;
  --blue-band:#2f7bac;
  --navy:#1f2f6e;
  --ink:#3c4350;
  --muted:#8a909a;
  --rule:#d6d8dc;
  --teal:#2fb3ad;
}
*{margin:0;padding:0;box-sizing:border-box}
html,body{width:855px;height:1200px;overflow:hidden}
body{background:var(--stage);font-family:"Montserrat",sans-serif;color:var(--ink);position:relative}
.slide{position:absolute;width:394px;height:222px;background:var(--white);overflow:hidden;box-shadow:0 2px 6px rgba(0,0,0,.25)}
.col-a{left:22px}.col-b{left:439px}
.row-1{top:228px}.row-2{top:490px}.row-3{top:752px}
.abs{position:absolute}
.photo{position:absolute}
.footer-page{position:absolute;left:16px;bottom:8px;font-size:3px;color:var(--muted)}
.footer-web{position:absolute;right:14px;bottom:8px;font-size:3px;color:var(--muted)}
.header-brand{position:absolute;left:16px;top:15px;font-size:3.4px;color:var(--muted)}
.header-brand b{color:var(--ink);font-weight:700}
.menu-icon{position:absolute;right:16px;top:12px;width:8px}
.menu-icon span{display:block;height:.7px;background:var(--muted);margin-bottom:1.6px}
.heading{font-weight:700;color:var(--blue);font-size:15.5px;white-space:nowrap}
.accent-bar{position:absolute;height:3px;background:var(--rule)}
.accent-bar i{position:absolute;top:0;height:3px;background:var(--blue)}

/* Cover */
.cover-photo{inset:0;background:
  radial-gradient(ellipse 70px 90px at 210px 30px,#2fb3ad 0%,#2aa5a0 60%,rgba(42,165,160,0) 100%),
  radial-gradient(ellipse 120px 60px at 140px 120px,#e7c9b4 0%,rgba(231,201,180,0) 100%),
  linear-gradient(160deg,#f5f7f9 0%,#e4e9ed 60%,#d9dfe4 100%)}
.cover-band{left:0;top:127px;width:379px;height:78px;background:var(--blue-band)}
.cover-band-edge{left:379px;top:127px;width:15px;height:78px;background:var(--navy)}
.cover-logo{left:268px;top:20px}
.cover-logo .name{font-weight:700;font-size:10px;color:var(--navy);white-space:nowrap}
.cover-logo .sub{font-size:2.4px;color:var(--navy);margin-top:1px;white-space:nowrap}
.doctor-mark{left:21px;top:150px;width:24px;height:24px;border:1.5px solid #fff;border-radius:50%}
.doctor-name{left:58px;top:154px;color:#fff;text-align:center;width:102px}
.doctor-name .pre{font-size:5px}
.doctor-name .nm{font-size:8.8px;font-weight:600;white-space:nowrap}
.doctor-name .fa{font-size:3.4px;font-weight:600;line-height:1.2;margin-top:1px}
.band-divider{left:152px;top:137px;width:.6px;height:58px;background:rgba(255,255,255,.7)}
.cover-text{left:168px;top:145px;color:#fff;width:200px}
.cover-text .kicker{font-size:5.6px;font-weight:600}
.cover-text h1{font-size:14px;font-weight:600;margin-top:3px;white-space:nowrap}
.cover-text p{font-size:3.4px;line-height:1.55;margin-top:4px;opacity:.9}

/* Welcome */
.welcome-photo{left:0;top:0;width:394px;height:105px;background:
  radial-gradient(ellipse 90px 60px at 40px 50px,#66755f 0%,rgba(102,117,95,0) 100%),
  radial-gradient(ellipse 70px 60px at 350px 55px,#5f6b59 0%,rgba(95,107,89,0) 100%),
  linear-gradient(90deg,#a3ac9f 0%,#d9dcd9 35%,#e8eae9 60%,#b9c0b6 85%,#8f998b 100%)}
.welcome{left:0;right:0;top:120px;text-align:center}
.welcome .sub{font-size:4.8px;color:var(--blue-band)}
.welcome h2{margin-top:4px}
.welcome p{font-size:4.6px;line-height:1.5;width:232px;margin:7px auto 0}

/* Table of content */
.toc-photo{left:212px;top:0;width:182px;height:222px;background:
  radial-gradient(ellipse 70px 90px at 130px 70px,#ffffff 0%,rgba(255,255,255,0) 100%),
  linear-gradient(180deg,#eef1f3 0%,#e1e5e9 55%,#cfd4d9 100%)}
.toc-kicker{left:84px;top:16px;font-size:2.6px;color:var(--muted)}
.toc-title{left:38px;top:21px}
.toc-list{left:52px;top:73px}
.toc-item{height:24.8px}
.toc-item .t{font-size:6.8px;font-weight:600;color:var(--blue);white-space:nowrap}
.toc-item .d{font-size:5.4px;color:var(--ink);margin:3px 0 0 12px;white-space:nowrap}

/* About */
.about-photo{left:0;top:36px;width:197px;height:153px;background:
  radial-gradient(ellipse 60px 30px at 120px 80px,#e6cdbd 0%,rgba(230,205,189,0) 100%),
  radial-gradient(ellipse 40px 20px at 80px 125px,#3f6b9c 0%,rgba(63,107,156,0) 100%),
  linear-gradient(180deg,#eceff2 0%,#f4f6f8 60%,#dfe4e9 100%)}
.about-title{left:224px;top:52px}
.about-text{left:224px;top:109px;width:154px;font-size:4px;line-height:2.2;text-align:justify}

/* Why us */
.why-title{left:36px;top:50px}
.why-item{left:38px;width:140px}
.why-item .t{font-size:4.2px;font-weight:700;color:var(--blue)}
.why-item p{font-size:3.8px;line-height:1.75;margin-top:3px;white-space:nowrap}
.portrait{background:linear-gradient(180deg,#eef1f4 0%,#d4dae0 52%,#27324e 62%,#1d2740 100%)}
.ghost-card{background:#fff;box-shadow:0 2px 6px rgba(0,0,0,.14)}

/* Features */
.features-photo{inset:0;background:linear-gradient(90deg,#f1f3f5,#e2e6ea)}
.features-band{left:0;top:37px;width:394px;height:159px;background:linear-gradient(90deg,#1f5b96,#2a6199)}
.features-band h2{position:absolute;left:26px;top:16px;font-size:15px;font-weight:600;color:#fff;white-space:nowrap}
.features-band p{position:absolute;left:26px;top:39px;font-size:3.8px;line-height:1.7;color:#fff;white-space:nowrap}
.feature-card{position:absolute;top:68px;width:111px;height:65px;background:#fff;padding:8px 12px}
.feature-card .n{font-size:13px;font-weight:500;color:#c5c9cf;line-height:1}
.feature-card .h{font-size:6.6px;color:var(--ink);margin-top:2px;white-space:nowrap}
.feature-card .d{font-size:3.8px;line-height:1.6;color:var(--muted);margin-top:4px}
</style>
</head>
<body>

<section class="slide col-a row-1">
  <div class="photo cover-photo" role="img" aria-label="Foto: Ärztin im Kittel mit Stethoskop beim Schreiben auf einem Klemmbrett"></div>
  <div class="abs cover-logo">
    <div class="name">Praxis am Lindengrund</div>
    <div class="sub">Dr. med. Jonas Fellbrunn | Innere- und Allgemeinmedizin</div>
  </div>
  <div class="abs cover-band"></div>
  <div class="abs cover-band-edge"></div>
  <div class="abs doctor-mark"></div>
  <div class="abs doctor-name">
    <div class="pre">Dr. med.</div>
    <div class="nm">Jonas Fellbrunn</div>
    <div class="fa">Facharzt für Innere-/Allgemein- und<br>Ernährungsmedizin</div>
  </div>
  <div class="abs band-divider"></div>
  <div class="abs cover-text">
    <div class="kicker">Medical Presentation</div>
    <h1>TITLE TEXT HERE</h1>
    <p>Lorem Ipsum is simply dummy text of the printing and typesetting industry. Lorem Ipsum<br>has been the industry's standard dummy text ever since the 1500s.</p>
  </div>
</section>

<section class="slide col-b row-1">
  <div class="photo welcome-photo" role="img" aria-label="Foto: Glastür der Praxis mit Pflanzen im Hintergrund"></div>
  <div class="abs welcome">
    <div class="sub">Insert Your Subtitle Here</div>
    <h2 class="heading">Welcome Message</h2>
    <p>Lorem Ipsum is simply dummy text of the printing and typesetting industry. Lorem Ipsum has been the industry's standard dummy text ever since the 1500s, when an unknown printer took a galley <b>of type and scrambled it to make a type.</b></p>
  </div>
  <div class="footer-page">Page | 2</div>
  <div class="footer-web">www.praxis-lindengrund.de</div>
</section>

<section class="slide col-a row-2">
  <div class="abs toc-kicker">Agenda</div>
  <h2 class="abs heading toc-title">Table Of Content</h2>
  <div class="accent-bar" style="left:0;top:53px;width:170px"><i style="left:0;width:47px"></i></div>
  <div class="abs toc-list">
    <div class="toc-item"><div class="t">01. Description</div><div class="d">Lorem Ipsum is simply dummy text</div></div>
    <div class="toc-item"><div class="t">02. Description</div><div class="d">Lorem Ipsum is simply dummy text</div></div>
    <div class="toc-item"><div class="t">03. Description</div><div class="d">Lorem Ipsum is simply dummy text</div></div>
    <div class="toc-item"><div class="t">04. Description</div><div class="d">Lorem Ipsum is simply dummy text</div></div>
    <div class="toc-item"><div class="t">05. Description</div><div class="d">Lorem Ipsum is simply dummy text</div></div>
  </div>
  <div class="photo toc-photo" role="img" aria-label="Foto: Arzt im Kittel hält eine Medikamentenschachtel vor einem Regal"></div>
  <div class="footer-page">Page | 3</div>
</section>

<section class="slide col-b row-2">
  <div class="header-brand"><b>PRAXISLINDENGRUND</b> | Medical Presentation</div>
  <div class="menu-icon"><span></span><span></span><span></span></div>
  <div class="photo about-photo" role="img" aria-label="Foto: Hände auf einem Tisch neben Stethoskop und Klemmbrett"></div>
  <h2 class="abs heading about-title">About Us</h2>
  <div class="accent-bar" style="left:224px;top:86px;width:87px"><i style="left:63px;width:24px"></i></div>
  <p class="abs about-text">Lorem ipsum dolor sit amet, consectetur adipiscing elit. Pellentesque scelerisqu malesua libero a pellentesque. Morbi orci dui, fermentum eget lectus ornareiui, viverra dignissim ris. Donec lacinia neq non velit dictum tincidunt. Etiam lacusiu neque, mattis ut sem sit amet, accumsan egestas nulla. Lorem ipsum fermentum eget lectus ornareiui</p>
  <div class="footer-page">Page | 4</div>
  <div class="footer-web">www.praxis-lindengrund.de</div>
</section>

<section class="slide col-a row-3">
  <div class="header-brand"><b>PRAXISLINDENGRUND</b> | Medical Presentation</div>
  <div class="menu-icon"><span></span><span></span><span></span></div>
  <h2 class="abs heading why-title">Why Us ?</h2>
  <div class="accent-bar" style="left:37px;top:84px;width:88px"><i style="left:64px;width:24px"></i></div>
  <div class="abs why-item" style="top:106px"><div class="t">Quality School</div><p>Lorem ipsum dolor sit amet, consectetur adipiscing elit<br>Pellentesque scelerisqu malesua libero a pellentesque</p></div>
  <div class="abs why-item" style="top:145px"><div class="t">Quality School</div><p>Lorem ipsum dolor sit amet, consectetur adipiscing elit<br>Pellentesque scelerisqu malesua libero a pellentesque</p></div>
  <div class="abs ghost-card" style="left:300px;top:35px;width:51px;height:51px"></div>
  <div class="abs ghost-card" style="left:200px;top:134px;width:51px;height:51px"></div>
  <div class="abs portrait" style="left:199px;top:35px;width:86px;height:86px" role="img" aria-label="Porträtfoto eines Arztes im dunklen Poloshirt"></div>
  <div class="abs portrait" style="left:266px;top:101px;width:86px;height:86px" role="img" aria-label="Porträtfoto eines Arztes mit Brille im dunklen Poloshirt"></div>
  <div class="footer-page">Page | 5</div>
  <div class="footer-web">www.praxis-lindengrund.de</div>
</section>

<section class="slide col-b row-3">
  <div class="photo features-photo" role="img" aria-label="Blasses Foto des Praxisempfangs im Hintergrund"></div>
  <div class="header-brand"><b>PRAXISLINDENGRUND</b> | Medical Presentation</div>
  <div class="menu-icon"><span></span><span></span><span></span></div>
  <div class="abs features-band">
    <h2>TITLE TEXT HERE</h2>
    <p>Lorem Ipsum has been the industry's standard dummy text ever since the<br>1500s. <b>It has survived not only five centuries, but also the leap into electronic.</b></p>
    <div class="feature-card" style="left:26px"><div class="n">01.</div><div class="h">Short Description</div><div class="d">Lorem Ipsum is simply dummy text of the printing and typesetting industry.</div></div>
    <div class="feature-card" style="left:143px"><div class="n">02.</div><div class="h">Short Description</div><div class="d">Lorem Ipsum is simply dummy text of the printing and typesetting industry.</div></div>
    <div class="feature-card" style="left:259px"><div class="n">03.</div><div class="h">Short Description</div><div class="d">Lorem Ipsum is simply dummy text of the printing and typesetting industry.</div></div>
  </div>
  <div class="footer-page">Page | 6</div>
  <div class="footer-web">www.praxis-lindengrund.de</div>
</section>

</body>
</html>
```